Kestrel Hitches Square Business Card Design

I would like a 2 x 2 square rounded corner business card.my business manufacture vehicle hitches and uses square tubing with rounded corners and would like to incorporate the border to look like the tubing...
4127 Larkfield Ave. Cedar Vale, Oregon 97035
(731) 555-0187
dale@kestrelhitches.example
www.kestrelhitches.example

Target Market(s)

automotive / vehicle hitches

Industry/Entity Type

Automotive

Contact Information for Business Card

I would like a 2 x 2 square rounded corner business card.my business manufacture vehicle hitches and uses square tubing with rounded corners and would like to incorporate the border to look like the tubing... and red, white and blue theme colors

Font styles to use
Sans Serif

Colors

Designer to choose colors to be used in the design.

Requirements
Must have
• Boarder
Nice to have
• red, white, blue theme colors
Should not have
• odd colors

```html
<!DOCTYPE html>
<html lang="en">
<head>
<meta charset="utf-8">
<title>Kestrel Hitches – Square Business Card</title>
<link href="https://fonts.googleapis.com/css2?family=Lato:wght@700;900&display=swap" rel="stylesheet">
<style>
  :root {
    --red: #e0202e;
    --navy: #1f3d7a;
    --ink: #1e1e1e;
    --paper: #ffffff;
    --stage: #e8e4de;
    --steel-light: #f4f4f4;
    --steel-mid: #bdbdbd;
    --steel-dark: #7c7c7c;
    --edge: #555555;
  }
  * { box-sizing: border-box; margin: 0; padding: 0; }
  html, body { width: 1200px; height: 618px; overflow: hidden; }
  body {
    background: var(--stage);
    font-family: "Lato", Arial, sans-serif;
    position: relative;
  }
  .card {
    position: absolute;
    top: 60px;
    width: 516px;
    height: 516px;
    border-radius: 46px;
    background: linear-gradient(135deg, var(--steel-light) 0%, var(--steel-mid) 22%, var(--steel-light) 45%, var(--steel-dark) 62%, var(--steel-light) 80%, var(--steel-mid) 100%);
    box-shadow: 0 6px 14px rgba(0,0,0,0.3), inset 0 0 0 2px rgba(255,255,255,0.6);
  }
  .card--front { left: 58px; }
  .card--back { left: 624px; }
  .card__face {
    position: absolute;
    inset: 28px;
    border-radius: 30px;
    background: var(--paper);
    border: 4px solid var(--edge);
    box-shadow: 0 0 0 3px rgba(255,255,255,0.7), inset 0 2px 4px rgba(0,0,0,0.15);
    text-align: center;
  }
  .line { position: absolute; left: 0; right: 0; font-weight: 700; white-space: nowrap; }
  .holder-name { top: 56px; font-size: 41px; line-height: 50px; color: var(--red); }
  .holder-role { top: 108px; font-size: 30px; line-height: 36px; color: var(--navy); }
  .address { top: 203px; font-size: 27px; line-height: 35px; color: var(--ink); }
  .contact { font-size: 25px; line-height: 34px; color: var(--ink); display: flex; justify-content: center; align-items: center; gap: 7px; }
  .contact--phone { top: 294px; font-size: 28px; }
  .contact--email { top: 330px; }
  .contact--web { top: 364px; }
  .contact svg { width: 20px; height: 20px; flex: none; }
  .brand-name {
    position: absolute; left: 0; right: 0; top: 134px;
    font-size: 84px; font-weight: 700; line-height: 92px; color: var(--navy);
  }
  .brand-web { top: 379px; font-size: 19px; line-height: 26px; color: var(--ink); }
</style>
</head>
<body>
  <section class="card card--front">
    <div class="card__face">
      <p class="line holder-name">Dale R. Whitford</p>
      <p class="line holder-role">Owner</p>
      <p class="line address">4127 Larkfield Ave.<br>Cedar Vale, Oregon 97035</p>
      <p class="line contact contact--phone">
        <svg viewBox="0 0 20 20" aria-hidden="true"><path fill="#e0202e" d="M2 8c0-3 3-5 8-5s8 2 8 5l-3 1-1-2c-2-1-6-1-8 0L5 9zM5 11h10l2 6H3z"/><circle cx="10" cy="14" r="2" fill="#fff"/></svg>
        (731) 555-0187
      </p>
      <p class="line contact contact--email">
        <svg viewBox="0 0 20 20" aria-hidden="true"><rect x="1.5" y="4" width="17" height="12" fill="none" stroke="#e0202e" stroke-width="2"/><path d="M1.5 4l8.5 7 8.5-7" fill="none" stroke="#e0202e" stroke-width="2"/></svg>
        dale@kestrelhitches.example
      </p>
      <p class="line contact contact--web">
        <svg viewBox="0 0 20 20" aria-hidden="true"><circle cx="10" cy="10" r="8.5" fill="#e0202e"/><ellipse cx="10" cy="10" rx="3.5" ry="8.5" fill="none" stroke="#fff" stroke-width="1.4"/><path d="M1.5 10h17" stroke="#fff" stroke-width="1.4"/></svg>
        www.kestrelhitches.example
      </p>
    </div>
  </section>

  <section class="card card--back">
    <div class="card__face">
      <p class="brand-name">Kestrel<br>Hitches</p>
      <p class="line brand-web">www.kestrelhitches.example</p>
    </div>
  </section>
</body>
</html>
```